brivox new business card design project

we need a new business card design. you can view info about us @ brivox.com. i have attached an example of our previous card with our previous name that we no longer use. We really liked the design, colors etc. look below to see more info about this project. it asks for a limited number of words. please see our website for more info about our compnay.

Target Market(s)

law enforcement

Contact Information for Business Card

i have uploaded an example of what we used before that we liked.

Font styles to use
Serif

```html
<!DOCTYPE html>
<html lang="en">
<head>
<meta charset="utf-8">
<title>Brivox Business Card</title>
<link rel="stylesheet" href="https://fonts.googleapis.com/css2?family=Libre+Baskerville:wght@400;700&display=swap">
<style>
  :root {
    --backdrop: #141414;
    --card: #262425;
    --card-back: #2b292a;
    --pattern-light: #3a3839;
    --pattern-dark: #232122;
    --ink: #ffffff;
    --ink-soft: #d9d9d9;
    --ink-muted: #8c8c8c;
    --rule: #bdbdbd;
  }
  * { box-sizing: border-box; margin: 0; padding: 0; }
  html, body {
    width: 1200px; height: 900px; overflow: hidden;
    background: radial-gradient(ellipse at 50% 35%, #242424 0%, var(--backdrop) 70%);
    font-family: "Libre Baskerville", Georgia, serif;
  }
  .card {
    position: absolute; left: 290px; width: 620px; height: 354px;
    box-shadow: 0 14px 30px rgba(0,0,0,.55);
  }
  .card-back { top: 60px; background: var(--card-back); }
  .card-front { top: 446px; background: var(--card); color: var(--ink); }

  .back-pattern {
    position: absolute; inset: 0;
    background: repeating-linear-gradient(60deg, var(--pattern-dark) 0 38px, var(--pattern-light) 38px 76px);
    opacity: .55;
  }
  .back-name {
    position: absolute; left: 0; right: 0; top: 162px;
    text-align: center; font-size: 19px; letter-spacing: 3px; color: var(--ink);
  }

  .brand-name {
    position: absolute; left: 40px; top: 40px;
    font-size: 52px; line-height: 1; letter-spacing: 6px; font-weight: 400; color: var(--ink);
  }
  .person { position: absolute; left: 40px; top: 198px; }
  .person-name { font-size: 24px; line-height: 1.2; font-weight: 700; }
  .person-title { font-size: 14px; line-height: 1.3; color: var(--ink-muted); }
  .divider {
    position: absolute; left: 40px; right: 40px; top: 258px;
    border-top: 1px solid var(--rule);
  }
  .contacts { position: absolute; left: 40px; top: 268px; list-style: none; }
  .contacts li {
    display: flex; align-items: center; gap: 12px;
    font-size: 13px; color: var(--ink-soft); height: 23px;
  }
  .contacts svg { width: 15px; height: 15px; flex: none; }
  .address {
    position: absolute; right: 40px; top: 292px;
    text-align: right; font-size: 13px; line-height: 20px; color: var(--ink-soft);
    font-style: normal;
  }
</style>
</head>
<body>
  <section class="card card-back">
    <div class="back-pattern" role="img" aria-label="Faint repeating pattern of the company name in diagonal columns"></div>
    <div class="back-name">BRIVOX</div>
  </section>

  <section class="card card-front">
    <div class="brand-name">BRIVOX</div>
    <div class="person">
      <div class="person-name">Daniel Reyes</div>
      <div class="person-title">President</div>
    </div>
    <div class="divider"></div>
    <ul class="contacts">
      <li>
        <svg viewBox="0 0 16 16" aria-hidden="true"><path fill="#d9d9d9" d="M3.5 1.5l2.4 2.8-1.3 1.6c.8 1.9 2.6 3.7 4.5 4.5l1.6-1.3 2.8 2.4-1.2 2.4C7.5 13.7 2.3 8.5 1.1 3.3z"/></svg>
        <span>866.555.0142</span>
      </li>
      <li>
        <svg viewBox="0 0 16 16" aria-hidden="true"><rect x="1" y="3.5" width="14" height="9" fill="none" stroke="#d9d9d9" stroke-width="1.2"/><path d="M1 3.5l7 5.5 7-5.5" fill="none" stroke="#d9d9d9" stroke-width="1.2"/></svg>
        <span>info@brivox.com</span>
      </li>
      <li>
        <svg viewBox="0 0 16 16" aria-hidden="true"><g fill="none" stroke="#d9d9d9" stroke-width="1.1"><circle cx="8" cy="8" r="6.5"/><ellipse cx="8" cy="8" rx="3" ry="6.5"/><path d="M1.5 8h13M2.5 4.8h11M2.5 11.2h11"/></g></svg>
        <span>brivox.com</span>
      </li>
    </ul>
    <address class="address">
      4120 Alder Ridge Road<br>
      Austin, TX 78704
    </address>
  </section>
</body>
</html>
```